Wordpress Design Project

The aim of our website is to provide information to a target market of people aged 17 - 22. We need the site to be appealing and also functional that contains a log in and possible forum so people can upload images and ideas. We have broken the information down into four categories and are looking for a website design somewhat like the following. Keeping in mind we are open to feedback from you and also ideas.

Website:
we need a word press design that contains the following:

- 1 main title page that contains a logo at the top centre and 4 main links with the mouse over function.

- all of the four links would then forward you to seperate pages that contain a slide bar at the top which enables the user to view different options. Once the user clicks on the option information will be provided below the scroll system. As well as the information we are looking to have a visual beside it, so a vidplume video beside it.

Target Market(s)

17 - 22 year olds

Industry/Entity Type

Vidplume

Requirements
Nice to have
• Forum and login

```html
<!DOCTYPE html>
<html lang="en">
<head>
<meta charset="utf-8">
<title>Pathwise School</title>
<link href="https://fonts.googleapis.com/css2?family=Fjalla+One&family=Encode+Sans+Condensed:wght@300&family=Arimo:wght@400;700&family=PT+Sans&display=swap" rel="stylesheet">
<style>
:root{
  --topbar:#4a4a4a;
  --header:#ececec;
  --green:#74c436;
  --green-dark:#5fa82a;
  --cyan:#1ec5d8;
  --yellow:#fdb913;
  --grey:#8b8b8b;
  --ink:#2e2e2e;
  --btn:#3f3f3f;
  --footer:#9a9a9a;
  --bottom:#383838;
  --white:#ffffff;
}
*{box-sizing:border-box;margin:0;padding:0}
html,body{width:1200px;height:1157px;overflow:hidden}
body{position:relative;background:linear-gradient(#f7f7f7,#ffffff 40%,#f1f1f1);font-family:"Arimo",Arial,sans-serif;color:var(--ink)}
.abs{position:absolute}
.topbar{left:0;top:0;width:1200px;height:35px;background:var(--topbar)}
.util-links{left:145px;top:10px;color:#fff;font-size:13px;letter-spacing:.2px}
.util-links span{margin:0 7px}
.follow-tab{left:862px;top:5px;width:191px;height:30px;background:var(--green);border-radius:5px 5px 0 0;display:flex;align-items:center;padding-left:22px;gap:6px;font-size:13px;color:#222}
.follow-tab .label{margin-right:8px}
.dot{width:20px;height:20px;border-radius:50%;background:#333}
.header{left:0;top:35px;width:1200px;height:115px;background:var(--header);border-bottom:1px solid #dcdcdc}
.nav a{position:absolute;top:52px;font-family:"Fjalla One",sans-serif;font-size:22px;color:var(--ink);text-decoration:none}
.brand{left:492px;top:78px;width:250px;display:flex;align-items:center;gap:10px;font-family:"Fjalla One",sans-serif;font-size:33px;color:var(--green-dark)}
.brand .mark{width:24px;height:24px;border-radius:50%;background:var(--green)}
.hero-frame{left:134px;top:182px;width:934px;height:290px;background:#888;border-radius:6px 6px 0 0}
.hero-inner{left:143px;top:190px;width:916px;height:258px;background:linear-gradient(100deg,#ffffff 30%,#e4e4e4 60%,#f2f2f2);border-radius:6px 6px 0 0}
.hero-text{left:179px;top:246px;width:500px;font-family:"Encode Sans Condensed",sans-serif;font-weight:300;font-size:30px;line-height:39px;color:#444}
.hero-photo{left:683px;top:226px;width:364px;height:222px;background:linear-gradient(120deg,#c9b3d6,#e8c06a 50%,#9fcf6a);border-radius:4px}
.steps{left:134px;top:447px;width:934px;height:97px;background:var(--green);border-radius:0 0 6px 6px}
.steps-shadow{left:156px;top:540px;width:892px;height:10px;background:#555;border-radius:0 0 10px 10px}
.steps-title{left:151px;top:466px;font-family:"Fjalla One",sans-serif;font-size:39px;line-height:48px;color:#fff}
.step{display:flex;align-items:center;gap:10px;top:476px}
.step .num{width:36px;height:36px;border-radius:50%;background:#fff;display:flex;align-items:center;justify-content:center;font-family:"Fjalla One",sans-serif;font-size:24px;color:#222}
.step p{font-size:13px;color:#fff;line-height:15px;width:120px}
.join{left:922px;top:474px;width:120px;height:42px;background:var(--btn);border-radius:5px;color:#fff;font-family:"Fjalla One",sans-serif;font-size:27px;text-align:center;line-height:42px}
.welcome h1{position:absolute;left:137px;top:566px;font-family:"Fjalla One",sans-serif;font-weight:400;font-size:28px;color:var(--ink)}
.welcome p{position:absolute;left:134px;top:604px;width:930px;font-family:"PT Sans",sans-serif;font-size:15px;line-height:17px;color:#222}
.card{top:688px;width:214px;height:204px}
.card .tab{height:46px;border-radius:10px 10px 0 0;padding:4px 16px;font-family:"Fjalla One",sans-serif;font-size:26px;color:#fff}
.card .body{position:absolute;top:43px;left:4px;right:0;height:161px;border-radius:12px 0 10px 10px;box-shadow:0 1px 3px rgba(0,0,0,.35);padding:15px 12px 0 15px}
.card h3{font-family:"Fjalla One",sans-serif;font-weight:400;font-size:16.5px;line-height:20px;color:var(--ink);white-space:nowrap}
.card p{margin-top:12px;font-family:"PT Sans",sans-serif;font-size:14.5px;line-height:16px;color:#222;white-space:nowrap}
.card .share{position:absolute;left:35px;top:185px;width:146px;height:27px;border-radius:14px;background:var(--btn);border:2px solid #222;color:#fff;font-family:"Encode Sans Condensed",sans-serif;font-size:16px;text-align:center;line-height:23px}
.footer{left:0;top:931px;width:1200px;height:177px;background:var(--footer)}
.fcol{top:945px}
.fcol h4{font-family:"Fjalla One",sans-serif;font-weight:400;font-size:18px;color:var(--ink);margin-bottom:12px}
.fcol li{list-style:none;font-size:11.5px;line-height:16.5px;color:#222}
.fcol p{font-size:11.5px;line-height:14px;color:#222}
.field{width:188px;height:18px;border-radius:9px;background:#fff;border:1px solid #666;font-size:11.5px;padding-left:11px;line-height:16px;margin-top:8px}
.submit{margin-top:11px;width:82px;height:22px;border-radius:11px;background:var(--btn);border:2px solid #222;color:#fff;font-family:"Fjalla One",sans-serif;font-size:14px;text-align:center;line-height:18px;letter-spacing:1px}
.socials{display:flex;gap:8px;margin-top:2px}
.socials .dot{width:30px;height:30px;background:#444}
.email{margin-top:14px;font-size:11.5px;color:#222}
.email span{color:#fff}
.bottombar{left:0;top:1108px;width:1200px;height:49px;background:var(--bottom);color:#ccc;font-size:11.5px;text-align:center;line-height:45px}
</style>
</head>
<body>
<div class="abs topbar"></div>
<div class="abs util-links">HOME <span>|</span> CONTACT US <span>|</span> LOGIN</div>
<div class="abs follow-tab"><span class="label">FOLLOW US:</span><i class="dot" role="img" aria-label="Social link"></i><i class="dot" role="img" aria-label="Social link"></i><i class="dot" role="img" aria-label="Vidplume"></i></div>

<header class="abs header">
  <nav class="nav">
    <a style="left:224px">Home</a>
    <a style="left:290px">Gap year</a>
    <a style="left:385px">Schoolies</a>
    <a style="left:760px">University</a>
    <a style="left:867px">Trades</a>
    <a style="left:945px">Forum</a>
  </nav>
</header>
<div class="abs brand"><i class="mark"></i>Pathwise School</div>

<div class="abs hero-frame"></div>
<div class="abs hero-inner"></div>
<div class="abs hero-text">Lorem ipsum dolor sit amet, consectetur<br>adipiscing elit. Vestibulum fermentum vitae<br>mi ut viverra.</div>
<div class="abs hero-photo" role="img" aria-label="Photo of a group of smiling students holding colourful notebooks"></div>

<div class="abs steps-shadow"></div>
<div class="abs steps"></div>
<div class="abs steps-title">Step to start :</div>
<div class="abs step" style="left:383px"><span class="num">1</span><p>Ut non mi sed ante lobortis volutpat.</p></div>
<div class="abs step" style="left:562px"><span class="num">2</span><p>Ut non mi sed ante lobortis volutpat.</p></div>
<div class="abs step" style="left:742px"><span class="num">3</span><p>Ut non mi sed ante lobortis volutpat.</p></div>
<div class="abs join">Join Now</div>

<section class="welcome">
  <h1>Welcome to Pathwise School</h1>
  <p>Sed consectetur nisi eget massa luctus tristique. Praesent tristique ipsum nulla, ut pellentesque lorem laoreet eu. Praesent ac magna a urna ultrices venenatis. Lorem ipsum dolor sit amet, consectetur adipiscing elit. Integer sit amet scelerisque quam, nec rutrum metus. Morbi convallis eu lacus eget placerat. Sed at condimentum velit. Phasellus scelerisque urna eget velit fermentum auctor. Sed a massa vel lacus accumsan rhoncus at id nulla.</p>
</section>

<div class="abs card" style="left:134px">
  <div class="tab" style="background:var(--grey)">Gap Years</div>
  <div class="body" style="background:#efefef"><h3>Is taking a gap year good<br>for you?</h3><p>Does taking a gap year after<br>high school make you a better<br>university student?</p></div>
  <div class="share">Share your experience</div>
</div>
<div class="abs card" style="left:373px">
  <div class="tab" style="background:var(--green)">Schoolies</div>
  <div class="body" style="background:#f2fde8"><h3>Integer pretium sem plac-<br>erat erat dum?</h3><p>Lorem ipsum dolor sit amet,<br>consectetur adipiscing elit.<br>Aenean?</p></div>
  <div class="share">Share your experience</div>
</div>
<div class="abs card" style="left:613px">
  <div class="tab" style="background:var(--cyan)">University</div>
  <div class="body" style="background:#dcfbfe"><h3>Lorem ipsum dolor sit am-<br>etscing elit?</h3><p>Nulla lacinia et justo nec ultri-<br>ces. Integer mollis tellus id<br>purus mattis?</p></div>
  <div class="share">Share your experience</div>
</div>
<div class="abs card" style="left:853px">
  <div class="tab" style="background:var(--yellow)">Trades</div>
  <div class="body" style="background:#fff2d4"><h3>Integer pretium sem plac-<br>erat erat dum?</h3><p>Lorem ipsum dolor sit amet,<br>consectetur adipiscing elit.<br>Aenean?</p></div>
  <div class="share">Share your experience</div>
</div>

<footer class="abs footer"></footer>
<div class="abs fcol" style="left:156px"><h4>Quick links</h4><ul><li>Home</li><li>Gap Years</li><li>Schoolies</li><li>University</li><li>Trades</li></ul></div>
<div class="abs fcol" style="left:390px"><h4>Information</h4><ul><li>FAQ</li><li>Contact</li><li>Terms of use</li><li>Privacy Policy</li></ul></div>
<div class="abs fcol" style="left:619px"><h4>Join us</h4><p>Lorem ipsum dolor sit amet,<br>consectetur adipiscing elit.</p><div class="field">Name</div><div class="field">Email Address</div><div class="submit">SUBMIT</div></div>
<div class="abs fcol" style="left:857px"><h4 style="margin-left:4px">Follow us</h4><div class="socials"><i class="dot" role="img" aria-label="Social link"></i><i class="dot" role="img" aria-label="Social link"></i><i class="dot" role="img" aria-label="Vidplume"></i></div><p class="email"><span>Email:</span> info@pathwiseschool.com</p></div>
<div class="abs bottombar">copyright 2013 pathwiseschool.com All Rights Reserved.</div>
</body>
</html>
```